Direct to Consumer extended service contract business with a new disruptive business model needs a

We need a customized wordpress design for a company called 'Tall Harbor Assurance'.
We provide an innovative and unique service contract protection program direct to consumers. This program provides monthly coverage for all electronics purchased in the last 4 years and all electronics the consumer purchases in the future for a low monthly fee. The overall design should communicate a sense of legitimacy, ethics, and superior customer service and support (in an industry that has a huge PR issue to overcome).
Electronics is the first product group, other product groups with different price points to launch in the future..

Target Market(s)

All purchasers of electronic goods...all demographics

Industry/Entity Type

Electronics

Font styles to use
Sans Serif

Requirements
Must have
• Customer Testimonials
Industry News
Customer ratings
Blog posts
Call to action messaging
Like the functional elements and design of bramblequill.example (need to be better)
Nice to have
• Like to see video testimonials
Social network "whats trending related to electronics or service contract industry"
Easy way to register products for warranty

```html
<!DOCTYPE html>
<html lang="en">
<head>
<meta charset="utf-8">
<title>Tall Harbor Assurance</title>
<link href="https://fonts.googleapis.com/css2?family=Alegreya+Sans:wght@400;500;700;800&display=swap" rel="stylesheet">
<style>
:root{
  --black:#000;
  --header:#111;
  --white:#fff;
  --ink:#111;
  --grey:#8a8a8a;
  --light-grey:#b9b9b9;
  --accent:#f0a51c;
  --brand:#6fd3a5;
  --btn-dark:#222;
  --fb:#3b5998;
  --tw:#2aa3d8;
  --gp:#d24a3b;
}
*{box-sizing:border-box;margin:0;padding:0}
html,body{width:1200px;height:3279px;overflow:hidden}
body{position:relative;background:var(--white);font-family:"Alegreya Sans",Arial,sans-serif;color:var(--ink)}
.abs{position:absolute}
.center{left:0;width:1200px;text-align:center}

/* header */
.site-header{position:absolute;top:0;left:0;width:1200px;height:120px;background:var(--header)}
.brand{position:absolute;left:179px;top:30px;display:flex;align-items:center;gap:14px}
.brand-mark{width:26px;height:26px;background:var(--brand)}
.brand-name{font-weight:800;font-size:34px;color:var(--brand);letter-spacing:1px;line-height:1}
.main-nav a{position:absolute;top:54px;color:var(--white);font-size:15px;font-weight:700;text-decoration:none}
.main-nav a.active{color:var(--accent)}
.main-nav a.active::after{content:"";position:absolute;left:0;right:0;top:24px;height:3px;background:var(--accent)}

/* hero */
.hero{position:absolute;top:120px;left:0;width:1200px;height:405px;background:var(--black)}
.hero-photo{position:absolute;left:547px;top:0;width:653px;height:405px;background:radial-gradient(ellipse at 60% 40%,#6a5d52 0%,#2f2924 45%,#000 85%)}
.hero-title{position:absolute;left:177px;top:62px;font-size:50px;font-weight:700;line-height:48px;color:var(--white)}
.hero-text{position:absolute;left:179px;top:184px;font-size:13px;line-height:16px;color:var(--light-grey);width:320px}
.btn-quote{position:absolute;left:179px;top:241px;width:125px;height:50px;border:3px solid var(--accent);color:var(--accent);font-weight:700;font-size:18px;display:flex;align-items:center;justify-content:center}
.arrow{position:absolute;width:30px;height:54px}

/* section titles */
.section-title{position:absolute;left:0;width:1200px;text-align:center;font-size:31px;font-weight:700;text-transform:uppercase}
.section-sub{position:absolute;left:270px;width:660px;text-align:center;font-size:13.5px;line-height:21px;font-weight:700;color:var(--grey)}
.dark{background:var(--black);color:var(--white)}
.dark .section-sub{color:var(--light-grey)}

/* news */
.news-image{position:absolute;left:179px;top:728px;width:416px;height:321px;background:radial-gradient(ellipse at 50% 45%,#3b6fc4 0%,#16274a 40%,#050505 80%)}
.news-heading{position:absolute;left:632px;top:722px;font-size:19px;font-weight:700}
.news-lead{position:absolute;left:632px;top:760px;width:390px;font-size:14px;line-height:20px;font-weight:700}
.news-body{position:absolute;left:632px;top:826px;width:390px;font-size:12.5px;line-height:20px;color:var(--light-grey)}
.btn-dark{position:absolute;left:632px;top:1003px;width:103px;height:46px;background:var(--btn-dark);color:var(--white);font-size:13px;font-weight:700;display:flex;align-items:center;justify-content:center;border-radius:3px}

/* testimonials */
.band{position:absolute;left:0;width:1200px}
.video{position:absolute;left:343px;top:1333px;width:499px;height:258px;background:linear-gradient(90deg,#3c3f44 0%,#5a5a5c 40%,#b7a089 60%,#4a4f55 100%)}

/* posts */
.post-img{position:absolute}
.post-title{position:absolute;font-size:19px;font-weight:700}
.post-meta{position:absolute;font-size:12px;color:var(--ink)}
.post-text{position:absolute;font-size:12.5px;line-height:19px;color:var(--light-grey)}
.share{position:absolute;width:42px;height:38px;border:2px solid;display:flex;align-items:center;justify-content:center}
.share.fb{border-color:var(--fb)}
.share.tw{border-color:var(--tw)}
.share.gp{border-color:var(--gp)}
.share span{width:10px;height:10px;border-radius:50%}
.share.fb span{background:var(--fb)}
.share.tw span{background:var(--tw)}
.share.gp span{background:var(--gp)}

/* ratings */
.rating{position:absolute;top:2525px;width:200px;margin-left:-100px;text-align:center}
.rating-name{font-size:19px;font-weight:700;color:var(--white)}
.rating-stars{font-size:11px;color:var(--accent);letter-spacing:1px;line-height:12px}

/* featuring */
.like-widget{position:absolute;left:463px;top:2804px;height:18px;display:flex;align-items:center;gap:6px;font-size:10.5px;color:var(--ink)}
.like-btn{width:38px;height:16px;border:1px solid #aab4c8;background:#eef1f7;border-radius:2px;font-size:10px;display:flex;align-items:center;justify-content:center;color:#3b4f7a}
.tile{position:absolute;top:2851px;height:183px}
.btn-cta{position:absolute;left:227px;top:2923px;width:175px;height:57px;border:3px solid var(--white);border-radius:4px;color:var(--white);font-size:18px;font-weight:700;display:flex;align-items:center;justify-content:center;text-transform:uppercase}

/* footer */
.site-footer{position:absolute;left:0;top:3089px;width:1200px;height:190px;background:var(--black);color:var(--white)}
.social{position:absolute;left:507px;top:47px;display:flex;gap:4px}
.social span{width:37px;height:37px;border:2px solid var(--white);border-radius:50%}
.footer-nav{position:absolute;top:108px;left:0;width:1200px;text-align:center;font-size:14px;font-weight:700}
.footer-nav a{color:var(--white);text-decoration:none;margin:0 17px}
.copyright{position:absolute;top:146px;left:0;width:1200px;text-align:center;font-size:13px;font-weight:700}
</style>
</head>
<body>

<header class="site-header">
  <div class="brand"><span class="brand-mark"></span><span class="brand-name">TALL HARBOR ASSURANCE</span></div>
  <nav class="main-nav">
    <a class="active" style="left:661px">Home</a>
    <a style="left:736px">Plans</a>
    <a style="left:806px">Benefits</a>
    <a style="left:894px">FAQs</a>
    <a style="left:963px">About Us</a>
  </nav>
</header>

<section class="hero">
  <div class="hero-photo" role="img" aria-label="Close-up of hands playing an acoustic guitar in low light"></div>
  <h1 class="hero-title">Coverage for all<br>Electronics</h1>
  <p class="hero-text">We provide service contract protection program direct to consumers.</p>
  <div class="btn-quote">Get Quote</div>
  <svg class="arrow" style="left:55px;top:153px" viewBox="0 0 30 54"><polyline points="28,2 3,27 28,52" fill="none" stroke="#777" stroke-width="2"/></svg>
  <svg class="arrow" style="left:1108px;top:153px" viewBox="0 0 30 54"><polyline points="2,2 27,27 2,52" fill="none" stroke="#777" stroke-width="2"/></svg>
</section>

<section class="news">
  <h2 class="section-title" style="top:594px">Industry News</h2>
  <p class="section-sub" style="top:646px">where you can shop for variety of products from across Mobiles &amp; Accessories, Computers &amp; Accessories, Cameras &amp; Photography, Portable Media Players and Personal Care Appliances.</p>
  <div class="news-image" role="img" aria-label="Laptops, tablets, phones and a GPS unit arranged on a reflective black surface"></div>
  <h3 class="news-heading">Consumer Electronics</h3>
  <p class="news-lead">Lorem Ipsum is simply dummy text of the printing and typesetting industry.</p>
  <p class="news-body">Every plan covers the devices you already own and the ones you buy next, with one low monthly fee and no hidden limits. Claims are handled quickly by a real support team, repairs come from trusted technicians and replacements ship fast when a fix is not possible.</p>
  <div class="btn-dark">View More</div>
</section>

<section class="band dark" style="top:1115px;height:557px"></section>
<h2 class="section-title" style="top:1176px;color:var(--white)">Customer Testimonials</h2>
<p class="section-sub" style="top:1232px;color:var(--light-grey)">Ut enim ad minima veniam, quis nostrum exercitationem ullam corporis suscipit laboriosam, nisi ut aliquid ex ea commodi consequatur? Quis autem vel eum iure reprehenderit</p>
<div class="video" role="img" aria-label="Video testimonial still of a customer wearing a headset at her desk"></div>
<svg class="abs" style="left:557px;top:1425px" width="80" height="80" viewBox="0 0 80 80"><circle cx="40" cy="40" r="35" fill="none" stroke="#fff" stroke-width="6"/><polygon points="31,22 58,40 31,58" fill="#fff"/></svg>
<svg class="arrow" style="left:262px;top:1435px" viewBox="0 0 30 54"><polyline points="28,2 3,27 28,52" fill="none" stroke="#777" stroke-width="2"/></svg>
<svg class="arrow" style="left:899px;top:1435px" viewBox="0 0 30 54"><polyline points="2,2 27,27 2,52" fill="none" stroke="#777" stroke-width="2"/></svg>

<section class="posts">
  <h2 class="section-title" style="top:1720px">Recent Post</h2>
  <p class="section-sub" style="top:1772px">Ut enim ad minima veniam, quis nostrum exercitationem ullam corporis suscipit laboriosam, nisi ut aliquid ex ea commodi consequatur? Quis autem vel eum iure reprehenderit</p>

  <div class="post-img" style="left:179px;top:1876px;width:461px;height:225px;background:linear-gradient(120deg,#e9e6e2 0%,#9a9590 35%,#2a2a2a 60%,#b8aa9c 100%)" role="img" aria-label="Hands using a touchscreen tablet"></div>
  <h3 class="post-title" style="left:179px;width:461px;text-align:center;top:2150px">Post With Large Image</h3>
  <p class="post-meta" style="left:179px;width:461px;text-align:center;top:2182px;color:var(--accent)">Aug 29 2014</p>
  <p class="post-text" style="left:200px;width:420px;text-align:center;top:2210px">Sed ut perspiciatis unde omnis iste natus error sit voluptatem accusantium doloremque laudantium, totam rem aperiam</p>
  <div class="share fb" style="left:328px;top:2282px"><span></span></div>
  <div class="share tw" style="left:389px;top:2282px"><span></span></div>
  <div class="share gp" style="left:448px;top:2282px"><span></span></div>

  <div class="post-img" style="left:667px;top:1876px;width:170px;height:201px;background:linear-gradient(90deg,#c9905a 0%,#f2e6d8 50%,#e0d6cc 100%)" role="img" aria-label="Woman reading on a tablet by a bright window"></div>
  <h3 class="post-title" style="left:863px;top:1870px">Post With Slider</h3>
  <p class="post-meta" style="left:863px;top:1908px">Posted by Aug 29, 201</p>
  <p class="post-text" style="left:863px;top:1945px;width:160px">At vero eos et accusamus et iusto odio dignissimos ducimus qui blanditiis</p>
  <div class="share fb" style="left:863px;top:2040px"><span></span></div>
  <div class="share tw" style="left:918px;top:2040px"><span></span></div>
  <div class="share gp" style="left:973px;top:2040px"><span></span></div>

  <div class="post-img" style="left:667px;top:2120px;width:170px;height:201px;background:linear-gradient(150deg,#7b7e82 0%,#2b2c2e 50%,#111 100%)" role="img" aria-label="Smartphone resting on a laptop keyboard"></div>
  <h3 class="post-title" style="left:863px;top:2115px">Post With Slider</h3>
  <p class="post-meta" style="left:863px;top:2152px">Posted by Aug 29, 201</p>
  <p class="post-text" style="left:863px;top:2190px;width:160px">At vero eos et accusamus et iusto odio dignissimos ducimus qui blanditiis</p>
  <div class="share fb" style="left:863px;top:2282px"><span></span></div>
  <div class="share tw" style="left:918px;top:2282px"><span></span></div>
  <div class="share gp" style="left:973px;top:2282px"><span></span></div>
</section>

<section class="band dark" style="top:2426px;height:188px"></section>
<h2 class="section-title" style="top:2461px;color:var(--white)">Customer Ratings</h2>
<div class="rating" style="left:385px"><div class="rating-name">Crestline Market</div><div class="rating-stars">★★★★★</div></div>
<div class="rating" style="left:614px"><div class="rating-name">Pinecone App Shelf</div><div class="rating-stars">★★★★★</div></div>
<div class="rating" style="left:820px"><div class="rating-name">Searchwell</div><div class="rating-stars">★★★★★</div></div>

<section class="featuring">
  <h2 class="section-title" style="top:2686px">Featuring Electronics</h2>
  <p class="section-sub" style="top:2738px">Ut enim ad minima veniam, quis nostrum exercitationem ullam corporis suscipit laboriosam, nisi ut aliquid ex ea commodi consequatur? Quis autem vel eum iure reprehenderit</p>
  <div class="like-widget"><span class="like-btn">Like</span><span>118,504 people like this. Be the first of your friends.</span></div>
  <div class="tile" style="left:179px;width:273px;background:linear-gradient(135deg,#3a3a3a 0%,#1a1a1a 100%)" role="img" aria-label="Dimmed photo of consumer electronics"></div>
  <div class="btn-cta">Call to Action</div>
  <div class="tile" style="left:463px;width:271px;background:linear-gradient(150deg,#2b2b2b 0%,#5d6f82 50%,#1c1c1c 100%)" role="img" aria-label="Hand holding a smartphone inside a car"></div>
  <div class="tile" style="left:745px;width:274px;background:linear-gradient(135deg,#e8e4df 0%,#b7aea5 55%,#6f6a66 100%)" role="img" aria-label="Hand using a stylus on a tablet beside a coffee cup"></div>
</section>

<footer class="site-footer">
  <div class="social"><span></span><span></span><span></span><span></span><span></span></div>
  <nav class="footer-nav"><a>Home</a><a>Plans</a><a>Benefits</a><a>FAQs</a><a>About Us</a></nav>
  <p class="copyright">© 2014 Tall Harbor Assurance</p>
</footer>

</body>
</html>
```